Business and Success Coaching Business Card

Need a business card for my coaching business. I coach small businesses, career professionals and, individuals wanting to unlock their human potential and achieve excellence. At the heart of our methodology is the Building Lasting Outcomes On Momentum (BLOOM) approach to formulate empowerment, create principles for success and setting achievable outcomes. I would like something that incorporates our new logo, something clean and sharp with a solid darker, but complementary background, color on the card front. The back should be white where there will be room for three questions

Target Market(s)

People looking to advance and improve themselves through a success coach

Industry/Entity Type

Life Coaching

Contact Information for Business Card

Contact information on card.
Business name on front of card
Questions on back

Font styles to use
Other font styles liked:
• Century Gothic or other Serif style fonts that look similar to Century Gothic

Colors

Designer to choose colors to be used in the design.

Requirements
Must have
• Logo on front of card
• Business name - The Bright Stride
• Contact name - Ray Dalton
• Address - Box 5196, Littleton, CO 80174-5196
• Phone number - 303-555-0148
• Email address - dalton.ray@thebrightstride.com
• Certifications - CSC, CCHt, PTT, PNLP
• Back of card
• Three questions on the back of the card:
• If you were at your best, what would you do right now?
• What is the decision you have been avoiding?
• What's one action you could take in the next 10 minutes?
Nice to have
• I would like to see a solid color on the front of the card that compliments the logo.
• Back should be white, or could be contrasting, but need to have the three questions.

```html
<!DOCTYPE html>
<html lang="en">
<head>
<meta charset="utf-8">
<title>The Bright Stride — Business Card</title>
<link href="https://fonts.googleapis.com/css2?family=Lato:wght@400;700;900&display=swap" rel="stylesheet">
<style>
  :root {
    --navy: #25336f;
    --sky: #3f86c9;
    --accent-text: #2f6fc0;
    --tagline: #9fb3dc;
    --paper: #ffffff;
    --stage: #2a2a2c;
    --ink: #2b3466;
  }
  * { margin: 0; padding: 0; box-sizing: border-box; }
  html, body { width: 1200px; height: 960px; overflow: hidden; }
  body {
    background: var(--stage);
    font-family: "Lato", sans-serif;
    position: relative;
  }
  .card {
    position: absolute;
    left: 304px;
    width: 594px;
    height: 339px;
    background: var(--paper);
    border-radius: 8px;
    overflow: hidden;
    box-shadow: 0 4px 14px rgba(0,0,0,0.5);
  }
  .card--front { top: 103px; }
  .card--back { top: 518px; }

  .band { position: absolute; inset: 0; width: 100%; height: 100%; }

  .holder { position: absolute; right: 16px; top: 24px; text-align: right; }
  .holder__name { font-weight: 900; font-size: 32px; color: var(--navy); letter-spacing: -0.3px; line-height: 1.1; }
  .holder__creds { font-size: 14px; color: var(--accent-text); margin-top: 2px; }

  .brand { position: absolute; left: 18px; top: 160px; width: 252px; text-align: center; }
  .brand__mark { display: inline-flex; align-items: center; gap: 8px; }
  .brand__dot { width: 14px; height: 14px; border-radius: 50%; background: var(--navy); }
  .brand__name { font-weight: 700; font-size: 25px; color: var(--navy); line-height: 1.1; }
  .brand__tagline { font-size: 14px; color: var(--tagline); line-height: 1.1; margin-top: 2px; }

  .contact { position: absolute; right: 16px; color: var(--paper); font-size: 14px; text-align: right; }
  .contact__address { top: 229px; }
  .contact__lines { top: 260px; list-style: none; }
  .contact__lines li { display: flex; align-items: center; justify-content: flex-end; gap: 10px; height: 21px; }
  .contact__lines svg { width: 12px; height: 12px; }

  .questions { position: absolute; left: 40px; top: 223px; list-style: none; color: var(--ink); font-size: 16px; }
  .questions li { height: 28px; }
</style>
</head>
<body>

<section class="card card--front" aria-label="Card front">
  <svg class="band" viewBox="0 0 594 339" preserveAspectRatio="none" aria-hidden="true">
    <path d="M0,262 C140,300 260,250 360,210 C440,182 520,178 594,196 L594,339 L0,339 Z" fill="var(--navy)"/>
  </svg>

  <div class="holder">
    <div class="holder__name">Ray Dalton</div>
    <div class="holder__creds">CSC, CCHt, PTT, PNLP</div>
  </div>

  <div class="brand">
    <div class="brand__mark">
      <span class="brand__dot"></span>
      <span class="brand__name">The Bright Stride</span>
    </div>
    <div class="brand__tagline">Move forward with purpose</div>
  </div>

  <div class="contact contact__address">Box 5196, Littleton, CO 80174-5196</div>
  <ul class="contact contact__lines">
    <li>303-555-0148
      <svg viewBox="0 0 12 12" aria-hidden="true"><path d="M3,1 L5,3.5 L4,4.8 C4.6,6 5.8,7.3 7.2,8 L8.5,7 L11,9 L9.8,11 C5,10.5 1.5,7 1,2.2 Z" fill="var(--paper)"/></svg>
    </li>
    <li>dalton.ray@thebrightstride.com
      <svg viewBox="0 0 12 12" aria-hidden="true"><rect x="0.5" y="2.5" width="11" height="7.5" fill="var(--paper)"/><path d="M0.5,2.5 L6,7 L11.5,2.5" fill="none" stroke="var(--navy)" stroke-width="1"/></svg>
    </li>
    <li>www.thebrightstride.com
      <svg viewBox="0 0 12 12" aria-hidden="true"><circle cx="6" cy="6" r="5" fill="none" stroke="var(--paper)" stroke-width="1"/><path d="M1,6 H11 M6,1 C3.5,4 3.5,8 6,11 M6,1 C8.5,4 8.5,8 6,11" fill="none" stroke="var(--paper)" stroke-width="0.8"/></svg>
    </li>
  </ul>
</section>

<section class="card card--back" aria-label="Card back">
  <ol class="questions">
    <li>If you were at your best, what would you do right now?</li>
    <li>What is the decision you have been avoiding?</li>
    <li>What's one action you could take in the next 10 minutes?</li>
  </ol>
</section>

</body>
</html>
```